Adorable Luxury Flower Shop

Need a beautiful, eye catching, elegant full-service website.
INSPIRATIONS ARE;
https://www.quillmoreblooms.com

Industry/Entity Type

retail, floral, boutique

Coding

Coded - Design and coding required

Number of Pages Required

3 page

Requirements
Must have
• SEO, Coded, UX, Fully responsive mobile, tablet, desktop, Ecommerce setup with Square, payments integration (if we use squarespace). SEO optimization with keywords, tags, meta descriptions, Load speed optimization, Google my business setup.
Nice to have
• pictures, color, elegance

```html
<!DOCTYPE html>
<html lang="en">
<head>
<meta charset="utf-8">
<title>Verdanelle Flower Boutique</title>
<link href="https://fonts.googleapis.com/css2?family=Jost:wght@400;500;600&family=Old+Standard+TT:wght@400;700&display=swap" rel="stylesheet">
<style>
:root{
  --red:#c0272d;
  --accent:#b5604f;
  --terracotta:#ad6454;
  --ink:#1d1d1d;
  --text:#555;
  --muted:#777;
  --soft:#f3f3f3;
  --foot:#f1eeec;
  --white:#fff;
}
*{margin:0;padding:0;box-sizing:border-box}
html,body{width:1200px;height:3861px;overflow:hidden}
body{position:relative;font-family:'Jost',sans-serif;color:var(--ink);background:var(--white)}
.abs{position:absolute}
.serif{font-family:'Old Standard TT',serif;font-weight:700}
.btn{position:absolute;background:var(--red);color:#fff;font-weight:600;font-size:15px;display:flex;align-items:center;justify-content:center;text-transform:uppercase}
.btn::after{content:"";position:absolute;inset:5px;border:2px solid #fff}
.rule{position:absolute;height:2px;background:var(--accent)}
.photo{position:absolute}
/* header */
.header{position:absolute;left:0;top:0;width:1200px;height:103px;background:#fff}
.brand{position:absolute;left:145px;top:30px;font-family:'Old Standard TT',serif;font-weight:700;font-size:24px;color:var(--ink)}
.nav a{position:absolute;top:42px;font-size:15px;color:var(--ink);text-decoration:none}
.nav a.active{color:var(--accent);text-decoration:underline}
.cart{position:absolute;left:997px;top:42px;font-size:11px;color:var(--muted);display:flex;gap:8px;align-items:center}
/* hero */
.hero{position:absolute;left:0;top:103px;width:1200px;height:579px;background:linear-gradient(90deg,#f6efec 0%,#eee3de 30%,#c9a48e 50%,#8fa46a 75%,#e9ebe3 100%)}
/* cards */
.card-bar{position:absolute;background:#fff;display:flex;align-items:center;justify-content:space-between;padding:0 20px;font-size:16px}
.product{position:absolute;width:216px;text-align:center}
.product .img{height:200px}
.product .name{margin-top:22px;font-size:16px}
.product .price{margin-top:8px;font-family:'Old Standard TT',serif;font-weight:700;color:var(--accent);font-size:17px;letter-spacing:1px}
.arrow-ic{position:absolute}
.testi{position:absolute;top:2753px;width:296px;height:182px;background:#fff;padding:25px 22px}
.stars{color:#f0a01c;font-size:17px;letter-spacing:5px}
.testi p{font-size:12.5px;line-height:24px;color:var(--text);margin-top:14px}
.testi .who{font-size:15px;margin-top:12px;color:var(--ink)}
.circ{position:absolute;width:36px;height:36px;border-radius:50%;display:flex;align-items:center;justify-content:center}
.fcol h4{font-weight:500;font-size:17px;margin-bottom:14px}
.fcol li{list-style:none;font-size:13px;color:var(--muted);height:27px}
.fcol li::before{content:"»";color:var(--accent);margin-right:14px}
.contact li::before{content:none}
</style>
</head>
<body>

<header class="header">
  <div class="brand">VERDANELLE</div>
  <div class="abs" style="left:168px;top:62px;font-size:7px;letter-spacing:2px;color:var(--accent)">FLOWER BOUTIQUE</div>
  <nav class="nav">
    <a class="active" style="left:340px">Home</a>
    <a style="left:411px">About Us</a>
    <a style="left:500px">Shop ⌄</a>
    <a style="left:586px">Spring</a>
    <a style="left:657px">Vase Arrangements</a>
    <a style="left:811px">Testimonials</a>
    <a style="left:917px">Contact</a>
  </nav>
  <div class="cart">
    <svg width="20" height="18" viewBox="0 0 20 18" fill="none" stroke="#b5604f" stroke-width="1.5"><path d="M1 1h3l2 11h11l2-8H5"/><circle cx="8" cy="16" r="1.3"/><circle cx="15" cy="16" r="1.3"/></svg>
    $0.00
  </div>
</header>

<section class="hero" role="img" aria-label="Smiling florist arranging a bouquet of lilies and white flowers"></section>
<div class="abs" style="left:144px;top:318px;color:var(--accent);font-size:16px;font-weight:500">Welcome To</div>
<h1 class="abs serif" style="left:144px;top:350px;font-size:44px;letter-spacing:1px">VERDANELLE</h1>
<div class="rule" style="left:145px;top:434px;width:96px"></div>
<p class="abs" style="left:145px;top:458px;width:420px;font-size:17px;line-height:28px;color:#333">Lorem ipsum dolor sit amet, consectetur adipiscing elit, sed do eiusmod tempor incididunt</p>
<div class="btn" style="left:145px;top:541px;width:152px;height:51px;font-size:16px">Shop Now</div>

<!-- about -->
<div class="photo" style="left:144px;top:761px;width:416px;height:364px;background:linear-gradient(160deg,#8a6d48,#3f5a4c 55%,#b9435c)" role="img" aria-label="Florist with arms crossed in front of a flower shop"></div>
<h2 class="abs serif" style="left:643px;top:780px;font-size:34px">ABOUT US</h2>
<div class="rule" style="left:643px;top:857px;width:100px"></div>
<p class="abs" style="left:645px;top:883px;width:412px;font-size:13px;line-height:24px;color:var(--text)">Lorem ipsum dolor sit amet, consectetur adipiscing elit, sed do eius­mod tempor incididunt ut labore et dolore magna aliqua. Ut enim ad minim veniam, quis nostrud exercitation ullamco laboris Sed ut per­spiciatis unde omnis iste natus error sit voluptatem accusantium do­loremque laudantium, totam rem aperiam, eaque</p>
<div class="btn" style="left:645px;top:1043px;width:137px;height:51px">Read More</div>

<!-- shop -->
<section class="abs" style="left:0;top:1207px;width:1200px;height:1370px;background:var(--soft)"></section>
<h2 class="abs serif" style="left:0;top:1278px;width:1184px;text-align:center;font-size:34px">SHOP FOR</h2>
<div class="rule" style="left:549px;top:1363px;width:101px"></div>

<div class="photo" style="left:144px;top:1418px;width:377px;height:279px;background:linear-gradient(135deg,#f1e8e3,#e8b8a6 50%,#6f8d63)" role="img" aria-label="Bride holding a peach and white rose bouquet"></div>
<div class="card-bar" style="left:144px;top:1697px;width:377px;height:49px">Weddings <svg width="20" height="14" viewBox="0 0 20 14" fill="none" stroke="#111" stroke-width="1.8"><path d="M1 7h17M12 1l6 6-6 6"/></svg></div>
<div class="photo" style="left:144px;top:1766px;width:377px;height:279px;background:linear-gradient(135deg,#d9d4cc,#c9a58e 50%,#d8333d)" role="img" aria-label="Couple sharing a bouquet of pink flowers"></div>
<div class="card-bar" style="left:144px;top:2045px;width:377px;height:50px">Sympathy Flowers <svg width="20" height="14" viewBox="0 0 20 14" fill="none" stroke="#111" stroke-width="1.8"><path d="M1 7h17M12 1l6 6-6 6"/></svg></div>
<div class="photo" style="left:537px;top:1418px;width:518px;height:627px;background:linear-gradient(170deg,#b9b8b4,#a9a7a2 50%,#d7a8b0 75%,#c8a886)" role="img" aria-label="Woman holding a wrapped bouquet of pink and cream flowers"></div>
<div class="card-bar" style="left:537px;top:2045px;width:518px;height:50px">Bouquets <svg width="20" height="14" viewBox="0 0 20 14" fill="none" stroke="#111" stroke-width="1.8"><path d="M1 7h17M12 1l6 6-6 6"/></svg></div>

<svg class="arrow-ic" style="left:104px;top:2206px" width="14" height="24" viewBox="0 0 14 24" fill="none" stroke="#111" stroke-width="2.5"><path d="M12 2 2 12l10 10"/></svg>
<svg class="arrow-ic" style="left:1082px;top:2206px" width="14" height="24" viewBox="0 0 14 24" fill="none" stroke="#111" stroke-width="2.5"><path d="M2 2l10 10-10 10"/></svg>

<div class="product" style="left:145px;top:2118px"><div class="img" style="background:linear-gradient(160deg,#e6e4e2,#eab6c0 55%,#dcdcd8)" role="img" aria-label="Pink carnations in a glass vase"></div><div class="name">Lorem ipsum dolor</div><div class="price">$150.00</div></div>
<div class="product" style="left:377px;top:2118px"><div class="img" style="background:radial-gradient(circle,#5f6b3e 20%,#d9435a 45%,#5a6a38 75%)" role="img" aria-label="Heart-shaped wreath of red and pink roses"></div><div class="name">Lorem ipsum dolor</div><div class="price">$150.00</div></div>
<div class="product" style="left:608px;top:2118px"><div class="img" style="background:linear-gradient(160deg,#b8121f,#d8222f 50%,#8f0d18)" role="img" aria-label="Bouquet of red roses"></div><div class="name">Lorem ipsum dolor</div><div class="price">$150.00</div></div>
<div class="product" style="left:840px;top:2118px"><div class="img" style="background:linear-gradient(160deg,#d9dfe2,#d96c9a 45%,#7aa152)" role="img" aria-label="Mixed pink and green flowers in a vase"></div><div class="name">Lorem ipsum dolor</div><div class="price">$150.00</div></div>

<div class="btn" style="left:500px;top:2444px;width:201px;height:50px">View More Flowers</div>

<!-- testimonials -->
<section class="abs" style="left:0;top:2577px;width:1200px;height:514px;background:var(--terracotta)"></section>
<h2 class="abs serif" style="left:0;top:2637px;width:1200px;text-align:center;font-size:34px;color:#fff;font-weight:400;letter-spacing:1px">CUSTOMERS TESTIMONIALS</h2>
<div class="abs" style="left:550px;top:2715px;width:100px;height:2px;background:#fff"></div>
<div class="testi" style="left:144px"><div class="stars">★★★★★</div><p>Lorem ipsum dolor sit amet, consectetur adipiscing elit, sed do eiusmod tempor incididunt ut labore et dolore.</p><div class="who">- Jess.L</div></div>
<div class="testi" style="left:452px"><div class="stars">★★★★★</div><p>Lorem ipsum dolor sit amet, consectetur adipiscing elit, sed do eiusmod tempor incididunt ut labore et dolore.</p><div class="who">- Goldberg.M</div></div>
<div class="testi" style="left:760px"><div class="stars">★★★★★</div><p>Lorem ipsum dolor sit amet, consectetur adipiscing elit, sed do eiusmod tempor incididunt ut labore et dolore.</p><div class="who">- Natasha,K</div></div>
<div class="circ" style="left:95px;top:2826px;border:1.5px solid #fff"><svg width="8" height="14" viewBox="0 0 8 14" fill="none" stroke="#fff" stroke-width="1.8"><path d="M7 1 1 7l6 6"/></svg></div>
<div class="circ" style="left:1068px;top:2826px;background:#fff"><svg width="8" height="14" viewBox="0 0 8 14" fill="none" stroke="#111" stroke-width="1.8"><path d="M1 1l6 6-6 6"/></svg></div>
<div class="btn" style="left:526px;top:2977px;width:149px;height:50px">Learn More</div>

<!-- newsletter -->
<h2 class="abs serif" style="left:0;top:3170px;width:1200px;text-align:center;font-size:38px">NEWSLETTER SIGNUP</h2>
<div class="rule" style="left:545px;top:3249px;width:110px"></div>
<p class="abs" style="left:0;top:3280px;width:1206px;text-align:center;font-size:13px;color:var(--text)">Stay Updated With our Latest Products and Offers!</p>
<div class="abs" style="left:316px;top:3336px;width:434px;height:52px;border:1px solid #ddd;font-size:12px;color:#aaa;padding:18px 19px">Enter your email</div>
<div class="btn" style="left:762px;top:3336px;width:121px;height:52px">Subscribe</div>

<!-- footer -->
<footer class="abs" style="left:0;top:3468px;width:1200px;height:393px;background:var(--foot)"></footer>
<div class="abs" style="left:144px;top:3573px;font-family:'Old Standard TT',serif;font-weight:700;font-size:25px">VERDANELLE</div>
<div class="circ" style="left:145px;top:3659px;background:#fff"></div>
<div class="circ" style="left:180px;top:3659px;background:var(--accent)"></div>
<div class="circ" style="left:220px;top:3659px;background:#fff"></div>
<div class="circ" style="left:261px;top:3659px;background:#fff"></div>

<div class="abs fcol" style="left:380px;top:3512px"><h4>Information</h4><ul><li>Home &amp; Lifestyle</li><li>About Us</li><li>Shop</li><li>Spring</li><li>Vase Arrangements</li><li>Testimonials</li><li>Contact</li></ul></div>
<div class="abs fcol" style="left:606px;top:3512px"><h4>Other Links</h4><ul><li>Site Map</li><li>Help Centre</li><li>Privacy Policy</li><li>Shipping &nbsp;Policy</li></ul></div>
<div class="abs fcol contact" style="left:832px;top:3512px"><h4>Contact Us</h4>
  <div style="font-size:13px;color:var(--muted);line-height:22px;display:flex;gap:10px"><svg width="10" height="14" viewBox="0 0 10 14" style="margin-top:4px"><path d="M5 0a5 5 0 0 0-5 5c0 4 5 9 5 9s5-5 5-9a5 5 0 0 0-5-5z" fill="#b5604f"/><circle cx="5" cy="5" r="1.8" fill="#f1eeec"/></svg><span>1-294 Lorem ipsum dolor sit amet,<br>consectetur adipiscing elit.</span></div>
  <div style="font-size:13px;color:var(--muted);margin-top:12px;display:flex;gap:12px;align-items:center"><svg width="12" height="12" viewBox="0 0 12 12"><path d="M2 1l2.5 0 1 3-1.5 1a7 7 0 0 0 3 3l1-1.5 3 1V11A10 10 0 0 1 1 2z" fill="#b5604f"/></svg>+1-888 888 8888</div>
  <div style="font-size:13px;color:var(--muted);margin-top:18px;display:flex;gap:12px;align-items:center"><svg width="12" height="10" viewBox="0 0 12 10"><rect width="12" height="10" fill="#b5604f"/><path d="M0 0l6 5 6-5" stroke="#f1eeec" fill="none"/></svg>info@verdanelle.com</div>
  <div style="font-size:13px;color:var(--muted);margin-top:18px;display:flex;gap:12px;align-items:center"><svg width="12" height="12" viewBox="0 0 12 12" fill="none" stroke="#b5604f" stroke-width="1.5"><circle cx="6" cy="6" r="5"/><path d="M6 3v3h2"/></svg>Mon - Sat : 8AM To 9 PM</div>
</div>

<div class="abs" style="left:144px;top:3761px;width:912px;height:1px;background:#999"></div>
<p class="abs" style="left:0;top:3781px;width:1200px;text-align:center;font-size:12.5px;color:var(--text)">Copyrights © Verdanelle. 2025 | Allrights Reserved</p>
<div class="abs" style="left:523px;top:3815px;display:flex;gap:5px">
  <span style="width:28px;height:16px;background:#2a4d9b"></span>
  <span style="width:28px;height:16px;background:#fff"></span>
  <span style="width:28px;height:16px;background:#2f79c9"></span>
  <span style="width:28px;height:16px;background:#fff"></span>
  <span style="width:28px;height:16px;background:#2a4d9b"></span>
</div>

</body>
</html>
```